Mother's Day Sale Banner Ad For Jewelry Site

We are looking for a designer to design a banner on our website advertising our Mother's Day Sale. I have enclosed a few pieces of jewelry we would like used in the ad. The ad size needs to be 1187 × 400. The ad should say:

Mother's Day Sale - Save 15% with Promo Code: LOVEMOM

Industry/Entity Type

Jewelry

```html
<!DOCTYPE html>
<html lang="en">
<head>
<meta charset="utf-8">
<title>Mother's Day Sale Banner</title>
<link rel="stylesheet" href="https://fonts.googleapis.com/css2?family=Lobster&display=swap">
<style>
  :root {
    --page: #ffffff;
    --raspberry: #cc1452;
    --ink: #2a1a1f;
    --paper: #ffffff;
    --mist: #f3f1f2;
    --silver: #c9c9cc;
    --steel: #4a4a4e;
    --gold: #d9b24a;
    --gold-deep: #a7801f;
    --skin: #f1d7cc;
    --skin-light: #fbf1ee;
  }
  * { margin: 0; padding: 0; box-sizing: border-box; }
  html, body {
    width: 1200px; height: 900px; overflow: hidden;
    background: var(--page);
  }
  .banner {
    position: absolute; left: 45px; top: 227px;
    width: 1103px; height: 373px;
    overflow: hidden;
    border: 1px solid #d6d6d6;
    background: var(--raspberry);
    font-family: 'Lobster', cursive;
  }
  .banner-shapes { position: absolute; inset: 0; }
  .jewelry-art {
    position: absolute; left: 38px; top: 138px;
    width: 355px; height: 215px;
    border-radius: 40px;
    background: radial-gradient(ellipse at 45% 50%, #f0d27a 0%, var(--gold) 45%, var(--gold-deep) 80%, rgba(167,128,31,0) 100%);
  }
  .headline {
    position: absolute; left: 220px; width: 490px; top: 52px;
    text-align: center; color: var(--ink); line-height: 1;
  }
  .headline-occasion { display: block; font-size: 60px; }
  .headline-sale { display: block; font-size: 96px; margin-top: -4px; }
  .promo-badge {
    position: absolute; left: 622px; top: 151px;
    width: 205px; height: 205px; border-radius: 50%;
    background: var(--paper);
    border: 6px solid var(--ink);
    display: flex; flex-direction: column; align-items: center; justify-content: center;
    text-align: center; line-height: 1.05;
  }
  .promo-save { color: var(--raspberry); font-size: 31px; }
  .promo-with { color: var(--ink); font-size: 25px; }
  .promo-code { color: var(--raspberry); font-size: 18px; margin-top: 2px; }
</style>
</head>
<body>
  <section class="banner">
    <svg class="banner-shapes" width="1103" height="373" viewBox="0 0 1103 373">
      <defs>
        <radialGradient id="portrait-tones" cx="45%" cy="45%" r="65%">
          <stop offset="0" stop-color="var(--skin-light)"/>
          <stop offset="0.6" stop-color="var(--skin)"/>
          <stop offset="1" stop-color="#e8c7ba"/>
        </radialGradient>
      </defs>
      <path class="backdrop-light" d="M20,0 C70,150 230,300 440,306 L780,290 L1103,255 L1103,0 Z" fill="var(--mist)"/>
      <path class="backdrop-silver-edge" d="M20,0 C70,150 230,300 440,306 L780,290" fill="none" stroke="var(--silver)" stroke-width="10"/>
      <path class="backdrop-steel-edge" d="M14,0 C64,154 226,306 440,313 L780,297" fill="none" stroke="var(--steel)" stroke-width="3"/>
      <circle class="portrait-ring-outer" cx="968" cy="215" r="200" fill="var(--paper)" stroke="var(--steel)" stroke-width="4"/>
      <circle class="portrait-ring-inner" cx="968" cy="215" r="178" fill="var(--paper)" stroke="var(--raspberry)" stroke-width="6"/>
      <circle class="portrait-photo" cx="968" cy="225" r="164" fill="url(#portrait-tones)" role="img" aria-label="Photo of a smiling mother and her baby lying together on white bedding"/>
    </svg>

    <div class="jewelry-art" role="img" aria-label="Photo of two gold rope rings crossed with diamond-set X bands"></div>

    <h1 class="headline">
      <span class="headline-occasion">Mother's Day</span>
      <span class="headline-sale">Sale</span>
    </h1>

    <div class="promo-badge">
      <span class="promo-save">Save 15%</span>
      <span class="promo-with">with Promo</span>
      <span class="promo-code">Code: LOVEMOM</span>
    </div>
  </section>
</body>
</html>
```